Anatomic 3D models + Urological Robotic surgery site

I want a website to represent my business as a developer of 3D models (reconstructions based on CT and MRI scans) and urological robotic surgery. The main point I need on my website is that it is modern, very attractive, clean, responsive and an interaction that differentiate me from the usual websites they have in my market. The site will be in portuguese and I'll provide the content to be used. The company name would be my name: Dr Rui Valmonte. The colors and other choices I made here are not final decisions. If you have a suggestion you, they are welcome.

My patients

Medical

Sans Serif

0054AA
0677BA
7BADD7
CADEEF
E8F1F8
0094D4
00A9DD
6FCCEA
C7EBF8
E9F6FB
00AB8E
00BBA5
67D7C9
C6EFE9
E9F9F6
59FF00
82FF00
B8FF75
E3FFCB
F4FFEA
FFC000
F8CF3A
FAE287
FDF2CF
FEFAEE
F0912C
F2A743
F7CA91
FBE8D2
FDF5EE
A7469A
B969AE
D3A5CF
EDDBEB
F8F0F9
6B429C
8869AF
B7A5CE
E3DAEB
F3F0F8

• Responsive, clean, modern, attractive, stand out from usual sites.
• Antiquate boring designs.

```html
<!DOCTYPE html>
<html lang="pt">
<head>
<meta charset="utf-8">
<title>Dr Rui Valmonte — Urologia e Cirurgia Robótica</title>
<link href="https://fonts.googleapis.com/css2?family=EB+Garamond:wght@600;700&family=Montserrat:wght@400;500;600;700;800&display=swap" rel="stylesheet">
<style>
:root{
  --green-dark:#0a6a55;
  --green:#06927a;
  --green-mid:#2a8a78;
  --gold:#f2b705;
  --ink:#1f5e50;
  --text:#5a6b66;
  --card-light:#e5efed;
  --white:#ffffff;
}
*{box-sizing:border-box;margin:0;padding:0}
html,body{width:1200px;height:5013px;overflow:hidden}
body{position:relative;background:var(--white);font-family:"Montserrat",sans-serif;color:var(--text);font-size:13px;line-height:1.5}
.abs{position:absolute}
.serif{font-family:"EB Garamond",serif;font-weight:700;color:var(--green-dark);line-height:1.05}
.eyebrow{font-size:12px;color:var(--gold);text-transform:uppercase;letter-spacing:.02em}
.photo{border-radius:22px;background:linear-gradient(140deg,#c9d4d6,#8aa3ab 55%,#5f7d86)}
.photo-round{border-radius:50%;border:6px solid #fff;background:linear-gradient(140deg,#d8d2c8,#9aa7a6)}
p.body{text-align:justify;margin-bottom:14px}

/* nav */
.nav{top:0;left:0;width:1200px;height:80px}
.logo{font-family:"EB Garamond",serif;font-weight:700;font-size:30px;color:var(--green-dark)}
.nav .logo{left:90px;top:18px}
.nav ul{list-style:none;display:flex;gap:33px;position:absolute;right:90px;top:30px;font-size:13px;color:#6d7a77}

/* hero */
.hero-left{left:0;top:80px;width:522px;height:529px;background:linear-gradient(135deg,#0d7b63,#3d9a89)}
.hero-right{left:522px;top:80px;width:678px;height:615px;background:var(--green);border-top-left-radius:120px;overflow:hidden}
.hero-text{left:90px;top:210px;width:560px;color:#fff}
.hero-text h1{font-family:"EB Garamond",serif;font-weight:600;font-size:54px;line-height:1.03;color:#fff;margin:14px 0 16px}
.hero-text hr{width:340px;border:0;border-top:1px solid rgba(255,255,255,.5);margin-bottom:22px}
.hero-text p{font-size:13px;line-height:1.75;width:400px}

/* intro */
.intro{left:190px;top:760px;width:820px;text-align:center;font-size:13px;line-height:1.5}
.intro p{margin-bottom:18px}
.feature{top:928px;width:312px;height:188px;border-radius:22px;color:#fff;text-align:center;padding:20px 26px}
.feature .icon{width:64px;height:64px;border-radius:50%;background:#fff;margin:0 auto 22px}
.feature p{font-size:13px;line-height:1.5}

/* band */
.band{left:0;top:1757px;width:1200px;height:524px;background:linear-gradient(180deg,#2b8a78,#0a6a55);color:#fff}
.band .serif{color:#fff}
.num{font-family:"Montserrat",sans-serif;font-weight:800;font-size:86px;line-height:1;background:linear-gradient(90deg,#c9a63a,#3aa587);-webkit-background-clip:text;background-clip:text;color:transparent}

/* care cards */
.care{top:3104px;width:456px;height:171px;border-radius:26px;background:var(--card-light);padding:18px 26px}
.care .icon{width:80px;height:80px;border-radius:50%;background:#fff;margin-bottom:16px}
.care p{font-size:13px;line-height:1.5}

ul.dots{list-style:none;margin-bottom:14px}
ul.dots li{position:relative;padding-left:18px;margin-bottom:12px;text-align:justify}
ul.dots li::before{content:"";position:absolute;left:0;top:6px;width:8px;height:8px;border-radius:50%;background:var(--gold)}

/* footer */
.footer{left:0;top:4534px;width:1200px;height:479px;background:var(--green-dark);color:#fff}
.footer-card{left:39px;top:53px;width:1123px;height:346px;border-radius:22px;background:#0e7460}
.footer .logo{color:#fff}
.footer h4{font-family:"EB Garamond",serif;font-weight:700;font-size:19px;margin-bottom:20px}
.footer ul{list-style:none;font-size:12.5px}
.footer li{margin-bottom:13px}
.social li{display:flex;align-items:center;gap:10px}
.social li span{width:14px;height:14px;border-radius:50%;background:var(--gold)}
.sub{left:78px;top:220px;width:416px;height:58px;border-radius:30px;background:#fff;color:#8a8a8a;font-size:12.5px;padding:20px 26px}
.sub b{position:absolute;right:6px;top:6px;height:46px;width:136px;border-radius:24px;background:var(--gold);color:#fff;font-size:12px;display:flex;align-items:center;justify-content:center;font-weight:700}
.totop{left:1090px;top:372px;width:42px;height:42px;border-radius:50%;background:var(--gold)}
</style>
</head>
<body>

<header class="abs nav">
  <div class="abs logo">Dr Rui Valmonte</div>
  <ul><li>Home</li><li>About Us</li><li>How We Operate</li><li>Planning</li><li>Pre Procedure</li><li>Postoperative Care</li></ul>
</header>

<section>
  <div class="abs hero-left"></div>
  <div class="abs hero-right">
    <svg width="678" height="615" class="abs" style="left:0;top:0">
      <path d="M420 -20 C470 120 620 160 700 120" stroke="#f2b705" stroke-width="2" fill="none"/>
      <path d="M640 140 C560 300 700 420 560 520 C500 560 470 580 460 615" stroke="#f2b705" stroke-width="2" fill="none"/>
      <circle cx="636" cy="402" r="9" fill="#f2b705"/>
      <circle cx="520" cy="576" r="9" fill="#f2b705"/>
    </svg>
    <div class="abs" role="img" aria-label="Equipamento de ressonância magnética" style="left:10px;top:60px;width:600px;height:400px;border-radius:40px;background:radial-gradient(ellipse at 65% 45%,#e9eef2,#b9c7d2 55%,rgba(6,146,122,0) 75%)"></div>
  </div>
  <div class="abs hero-text">
    <div class="eyebrow">Welcome to</div>
    <h1>Cuidar com precisão,<br>tratar com empatia</h1>
    <hr>
    <p>A cirurgia robótica representa um dos avanços mais relevantes da medicina moderna. Ela oferece mais precisão, menor sangramento e uma recuperação mais rápida. Mas, acima da tecnologia, está o compromisso com a melhor decisão para cada paciente.</p>
  </div>
</section>

<section>
  <div class="abs intro">
    <p>Aqui, entendemos que nem todo caso precisa de cirurgia, e muito menos que toda cirurgia precisa ser robótica. Trabalhamos com base nas melhores evidências científicas, diretrizes internacionais e, quando necessário, com o apoio de tecnologias de inteligência artificial para ajudar na definição da conduta mais adequada.</p>
    <p>Cada paciente é único. Por isso, antes de qualquer decisão, buscamos entender com profundidade a doença, os exames e, principalmente, as expectativas e prioridades de quem nos procura. Essa escuta atenta é o primeiro passo para uma escolha segura e compartilhada.</p>
  </div>
  <div class="abs feature" style="left:107px;background:var(--green)"><div class="icon" role="img" aria-label="Ícone de equipe administrativa"></div><p>Um time administrativo que cuida de todo o contato com hospitais e convênios, evitando desgastes com burocracias.</p></div>
  <div class="abs feature" style="left:444px;background:var(--green-dark)"><div class="icon" role="img" aria-label="Ícone de enfermeira"></div><p>Um grupo de enfermeiras e fisioterapeutas que acompanham o pós-operatório com visitas e orientações em domicílio.</p></div>
  <div class="abs feature" style="left:780px;background:var(--green)"><div class="icon" role="img" aria-label="Ícone de conversa"></div><p>Um canal de contato direto para esclarecer dúvidas e garantir tranquilidade durante todo o processo.</p></div>
</section>

<section>
  <div class="abs photo" role="img" aria-label="Médica conversando com paciente idoso" style="left:193px;top:1233px;width:402px;height:425px"></div>
  <div class="abs photo-round" role="img" aria-label="Retrato do médico" style="left:154px;top:1210px;width:222px;height:222px"></div>
  <div class="abs" style="left:644px;top:1284px;width:403px">
    <div class="eyebrow">Sobre mim</div>
    <h2 class="serif" style="font-size:38px;margin:12px 0 24px">Cuidar com precisão,<br>tratar com empatia</h2>
    <p class="body">Sou urologista com foco em cirurgia robótica e atenção integral ao paciente. Mais do que uma técnica, acredito que a boa medicina começa pela escuta, pelo planejamento cuidadoso e pelo compromisso com o que há de melhor para cada pessoa.</p>
    <p class="body">Minha missão é oferecer tratamentos baseados em ciência, tecnologia e humanidade — respeitando o tempo, as escolhas e os objetivos de cada paciente.</p>
  </div>
</section>

<section class="abs band">
  <div class="abs eyebrow" style="left:97px;top:52px">Como atuamos</div>
  <h2 class="abs serif" style="left:97px;top:84px;font-size:39px">Nem todo tratamento precisa<br>ser cirúrgico.</h2>
  <p class="abs" style="left:656px;top:97px;width:450px;font-size:13px">A cirurgia robótica é um grande avanço, mas deve ser indicada com critério. Antes de propor qualquer intervenção, avaliamos o caso de forma ampla:</p>
  <div class="abs" style="left:97px;top:195px;width:1014px;border-top:1px solid rgba(255,255,255,.25)"></div>
  <div class="abs num" style="left:97px;top:245px">01</div>
  <div class="abs num" style="left:453px;top:245px">02</div>
  <div class="abs num" style="left:848px;top:245px">03</div>
  <p class="abs" style="left:97px;top:335px;width:240px;font-size:12.5px">Utilizamos os guidelines médicos mais atualizados;</p>
  <p class="abs" style="left:453px;top:335px;width:300px;font-size:12.5px">Fazemos uso de ferramentas de inteligência artificial para apoiar a decisão clínica;</p>
  <p class="abs" style="left:848px;top:335px;width:270px;font-size:12.5px">Conduzimos conversas francas sobre as reais necessidades, benefícios e riscos de cada abordagem.</p>
  <p class="abs" style="left:90px;top:433px;width:700px;font-size:12.5px">Nosso foco é garantir que o paciente seja encaminhado à opção com maior potencial de resultado — seja ela cirúrgica, clínica ou mesmo vigilância ativa.</p>
</section>

<section>
  <div class="abs" style="left:193px;top:2421px;width:402px">
    <div class="eyebrow">Planejar com profundidade</div>
    <h2 class="serif" style="font-size:38px;margin:12px 0 24px">Planejamento com<br>Tecnologia 3D</h2>
    <p class="body">Em cirurgias renais e prostáticas, adotamos o uso de modelos 3D personalizados, criados a partir dos exames do próprio paciente.</p>
    <p class="body">Esses modelos ajudam a compreender a anatomia de forma precisa, facilitando a escolha da melhor abordagem cirúrgica.</p>
    <p class="body">Já demonstramos que esse planejamento reduz sangramentos, o tempo cirúrgico e até mesmo muda a estratégia em quase metade dos casos avaliados.</p>
  </div>
  <div class="abs photo" role="img" aria-label="Médico analisando exames em tablet" style="left:644px;top:2370px;width:403px;height:452px"></div>
</section>

<section>
  <div class="abs" style="left:0;top:2911px;width:1200px;text-align:center">
    <div class="eyebrow">Apoio pré-procedimento</div>
    <h2 class="serif" style="font-size:38px;margin:12px 0 16px">Seu foco deve ser sua saúde,<br>não a burocracia.</h2>
    <p style="font-size:13px">Sabemos que o momento que antecede um procedimento pode ser cercado de dúvidas<br>e ansiedade. Por isso, oferecemos:</p>
  </div>
  <div class="abs care" style="left:132px"><div class="icon" role="img" aria-label="Ícone de documentos"></div><p>Um escritório dedicado a resolver toda a parte burocrática com hospitais e convênios;</p></div>
  <div class="abs care" style="left:611px"><div class="icon" role="img" aria-label="Ícone de suporte"></div><p>Suporte próximo, ágil e humano, para que você se concentre no que realmente importa: sua preparação e bem-estar.</p></div>
</section>

<section>
  <div class="abs photo" role="img" aria-label="Médico acompanhando paciente no leito" style="left:193px;top:3395px;width:402px;height:477px"></div>
  <div class="abs photo-round" role="img" aria-label="Enfermeira com paciente idosa" style="left:154px;top:3372px;width:222px;height:222px"></div>
  <div class="abs" style="left:644px;top:3444px;width:403px">
    <div class="eyebrow">Cuidado no pós-operatório</div>
    <h2 class="serif" style="font-size:38px;margin:12px 0 24px">Recuperar bem é parte<br>essencial do tratamento.</h2>
    <p class="body">Após a alta hospitalar, continuamos ao seu lado. Nosso time de enfermeiras e fisioterapeutas oferece:</p>
    <ul class="dots">
      <li>Visitas domiciliares quando necessário;</li>
      <li>Orientações práticas sobre movimentação, alimentação e medicações;</li>
      <li>Monitoramento de sinais que mereçam atenção — sempre com o olhar clínico atento.</li>
    </ul>
    <p class="body">Além disso, mantemos um canal direto de contato para esclarecer dúvidas, adaptar condutas e apoiar sua recuperação.</p>
  </div>
</section>

<section>
  <div class="abs" style="left:193px;top:4026px;width:402px">
    <div class="eyebrow">Compromisso com o paciente</div>
    <h2 class="serif" style="font-size:38px;margin:12px 0 24px">Pode ser o fechamento<br>da homepage ou um<br>manifesto resumido</h2>
    <p class="body">Acreditamos que o melhor resultado vem da soma entre conhecimento, tecnologia e empatia.</p>
    <p class="body">Nosso compromisso é entender profundamente o que você está enfrentando, apresentar com clareza todas as opções disponíveis e construir, juntos, o melhor caminho para o seu tratamento.</p>
    <p class="body">Porque cada paciente é único — e merece ser cuidado como tal.</p>
  </div>
  <div class="abs photo" role="img" aria-label="Médico cumprimentando paciente idoso" style="left:644px;top:3974px;width:403px;height:453px"></div>
</section>

<footer class="abs footer">
  <div class="abs footer-card">
    <div class="abs logo" style="left:78px;top:128px">Dr Rui Valmonte</div>
    <p class="abs" style="left:78px;top:182px;font-size:13px">Subscribe to our newsletter for the latest updates</p>
    <div class="abs sub">Your Email Here<b>SUBSCRIBE</b></div>
    <p class="abs" style="left:78px;top:295px;font-size:9.5px;opacity:.85">By subscribing, you consent to our Privacy Policy and agree to receive updates.</p>
    <div class="abs" style="left:573px;top:95px"><h4>Quick Links</h4><ul><li>Home</li><li>About Us</li><li>How We Operate</li><li>Planning</li><li>Pre Procedure</li><li>Postoperative Care</li></ul></div>
    <div class="abs" style="left:749px;top:95px"><h4>Resources</h4><ul><li>FAQs</li><li>Appointment</li><li>Pricing Plan</li><li>Event</li><li>Community</li></ul></div>
    <div class="abs" style="left:904px;top:95px"><h4>Connect With Us</h4><ul class="social"><li><span></span>Friendspace</li><li><span></span>Chirper</li><li><span></span>Chatline</li><li><span></span>Wiremsg</li><li><span></span>Worknet</li></ul></div>
  </div>
  <div class="abs totop"><svg width="42" height="42"><path d="M16 24 L21 19 L26 24" stroke="#fff" stroke-width="2" fill="none"/></svg></div>
  <p class="abs" style="left:117px;top:433px;font-size:12px">Copyright © 2025 Dr Rui Valmonte. All Rights Reserved.</p>
  <p class="abs" style="left:752px;top:433px;font-size:12px">Privacy Policy &nbsp;|&nbsp; Terms of Service &nbsp;|&nbsp; Cookie Settings</p>
</footer>

</body>
</html>
```